Business Card Design Project

I am community manager and social media strategist. I need a double sided business card with company logo and name. Looking for something professional, elegant but also a little bit original.

• - The logo and the colours are the company colours and a required to stay.
- The size should be: 84 x 55 mm (or 3.30 x 2.16)
- The file size should be: 1039 x 697 pixels (300 dpi)
- I'd like rounded corners. :)

Use the following contact information for the card:

Léonie Vardin
Stratégie médias sociaux / community management / édition de sites sociaux
mob. : 0687529103
leonie.vardin@postelune.fr
Chirpline. : @lvardin
Callora : vardin.leonie

```html
<!DOCTYPE html>
<html lang="fr">
<head>
<meta charset="utf-8">
<title>Ventara – Léonie Vardin</title>
<link rel="stylesheet" href="https://fonts.googleapis.com/css2?family=Open+Sans:ital,wght@0,400;0,600;0,700;1,400&display=swap">
<style>
  :root {
    --page: #ffffff;
    --blue-deep: #245a94;
    --blue-mid: #2f6ea8;
    --blue-light: #3a82ba;
    --card-grey: #e6e7e8;
    --brand-blue: #235a97;
    --accent: #4a9fd8;
    --ink: #1d1d1f;
  }
  * { box-sizing: border-box; margin: 0; padding: 0; }
  html, body {
    width: 1200px;
    height: 401px;
    overflow: hidden;
    background: var(--page);
    font-family: "Open Sans", sans-serif;
  }
  .sheet { position: relative; width: 1200px; height: 401px; }

  .card {
    position: absolute;
    top: 22px;
    width: 537px;
    height: 352px;
    border-radius: 38px;
    overflow: hidden;
  }

  /* Front */
  .card--front {
    left: 34px;
    background: linear-gradient(135deg, var(--blue-deep) 0%, var(--blue-mid) 55%, var(--blue-light) 100%);
  }
  .card--front .sweep { position: absolute; inset: 0; }
  .front-brand {
    position: absolute;
    inset: 0;
    display: flex;
    align-items: center;
    justify-content: center;
    gap: 18px;
  }
  .front-brand__dot {
    width: 46px; height: 46px;
    border-radius: 50%;
    background: #eef0f2;
  }
  .front-brand__name {
    font-weight: 700;
    font-size: 52px;
    letter-spacing: 2px;
    color: #eef0f2;
  }

  /* Back */
  .card--back {
    left: 629px;
    background: var(--card-grey);
  }
  .brand {
    position: absolute;
    left: 30px;
    top: 58px;
    display: flex;
    align-items: center;
    gap: 24px;
  }
  .brand__dot {
    width: 72px; height: 72px;
    border-radius: 50%;
    background: var(--accent);
  }
  .brand__name {
    font-weight: 700;
    font-size: 50px;
    line-height: 60px;
    letter-spacing: 2px;
    color: var(--brand-blue);
  }

  .person {
    position: absolute;
    left: 296px;
    top: 150px;
  }
  .person__name {
    font-weight: 700;
    font-size: 20px;
    letter-spacing: 0.5px;
    line-height: 26px;
    color: var(--brand-blue);
    padding-left: 54px;
  }
  .services { list-style: none; }
  .services li {
    font-style: italic;
    font-size: 15px;
    line-height: 16.5px;
    color: var(--ink);
    white-space: nowrap;
  }
  .services li::before { content: "*"; color: var(--accent); font-style: normal; }

  .contact {
    position: absolute;
    top: 277px;
    font-size: 16.5px;
    line-height: 21px;
    color: var(--ink);
    white-space: nowrap;
  }
  .contact--phone { left: 67px; }
  .contact--social { left: 322px; }
  .contact__label { color: var(--accent); margin-right: 4px; }
  .contact__value--italic { font-style: italic; }
</style>
</head>
<body>
<main class="sheet">

  <section class="card card--front" aria-label="Recto de la carte">
    <svg class="sweep" width="537" height="352" viewBox="0 0 537 352" aria-hidden="true">
      <path d="M0 120 C 160 170, 360 200, 537 290 L 537 352 L 0 352 Z" fill="#ffffff" fill-opacity="0.05"/>
      <path d="M260 175 C 360 190, 460 230, 537 285 L 537 352 L 300 352 Z" fill="#ffffff" fill-opacity="0.05"/>
    </svg>
    <div class="front-brand">
      <span class="front-brand__dot"></span>
      <span class="front-brand__name">VENTARA</span>
    </div>
  </section>

  <section class="card card--back" aria-label="Verso de la carte">
    <div class="brand">
      <span class="brand__dot"></span>
      <span class="brand__name">VENTARA</span>
    </div>

    <div class="person">
      <h1 class="person__name">Léonie Vardin</h1>
      <ul class="services">
        <li>Stratégie médias sociaux</li>
        <li>Community management</li>
        <li>Édition de sites sociaux</li>
      </ul>
    </div>

    <p class="contact contact--phone">
      <span class="contact__label">mob:</span> 0687529103<br>
      <span class="contact__label">@:</span> leonie.vardin@postelune.fr
    </p>
    <p class="contact contact--social">
      <span class="contact__label">Chirpline:</span> @lvardin<br>
      <span class="contact__label">Callora:</span> <span class="contact__value--italic">vardin.leonie</span>
    </p>
  </section>

</main>
</body>
</html>
```